Business Card Design for Denton Vale Plaster Designs

We sell decorative plasterwork for home interior. We're an upmarket company and have been selling for over 30 years. Products include Cornice, Fireplaces, Domes, Arches, Ceiling Roses, Beading, Columns... please view our website [login to view URL]

```html
<!DOCTYPE html>
<html lang="en">
<head>
<meta charset="utf-8">
<title>Denton Vale Plaster Designs – Business Card</title>
<link href="https://fonts.googleapis.com/css2?family=Poiret+One&family=Questrial&family=Arimo&display=swap" rel="stylesheet">
<style>
  :root {
    --backdrop: #e9e6e1;
    --card-light: #b9bcbe;
    --card-dark: #9fa3a6;
    --ink: #1d1d1f;
    --ink-soft: #2e2f31;
    --accent: #f6c592;
    --rule: #d9dadb;
  }
  * { margin: 0; padding: 0; box-sizing: border-box; }
  html, body { width: 1200px; height: 840px; overflow: hidden; }
  body { background: var(--backdrop); position: relative; }

  .card {
    position: absolute;
    width: 560px;
    height: 320px;
    background: linear-gradient(135deg, var(--card-light) 0%, var(--card-dark) 100%);
    box-shadow: 0 6px 18px rgba(0,0,0,0.18);
  }
  .card--front { left: 50px; top: 90px; }
  .card--back  { left: 590px; top: 430px; }

  /* Front: brand name */
  .brand {
    position: absolute;
    left: 50px; top: 92px;
    display: flex; align-items: center; gap: 26px;
  }
  .brand__mark {
    width: 74px; height: 74px;
    background: var(--accent);
  }
  .brand__name {
    font-family: "Poiret One", sans-serif;
    color: var(--ink);
    line-height: 1;
  }
  .brand__primary { display: block; font-size: 62px; letter-spacing: 1px; }
  .brand__secondary { display: block; font-size: 30px; letter-spacing: 7px; text-transform: uppercase; margin-top: 8px; }

  /* Back: contact */
  .back__mark {
    position: absolute;
    left: 62px; top: 128px;
    width: 84px; height: 84px;
    background: var(--accent);
  }
  .back__rule {
    position: absolute;
    left: 200px; top: 108px;
    width: 1px; height: 180px;
    background: var(--rule);
  }
  .contact {
    position: absolute;
    left: 220px; top: 56px;
    color: var(--ink-soft);
  }
  .contact__name {
    font-family: "Questrial", sans-serif;
    font-size: 34px;
    color: var(--ink);
    margin-bottom: 22px;
  }
  .contact__lines {
    font-family: "Arimo", sans-serif;
    font-size: 14px;
    line-height: 1.42;
    list-style: none;
  }
  .contact__lines .gap { margin-top: 6px; }
</style>
</head>
<body>
  <section class="card card--front" aria-label="Card front">
    <div class="brand">
      <div class="brand__mark"></div>
      <h1 class="brand__name">
        <span class="brand__primary">Denton Vale</span>
        <span class="brand__secondary">Plaster Designs</span>
      </h1>
    </div>
  </section>

  <section class="card card--back" aria-label="Card back">
    <div class="back__mark"></div>
    <div class="back__rule"></div>
    <div class="contact">
      <h2 class="contact__name">YourName Here</h2>
      <ul class="contact__lines">
        <li>Your adress here, 123 Street</li>
        <li>Town, Country</li>
        <li>Tel: +00 123 456 789</li>
        <li>Fax: +00 123 456 789</li>
        <li class="gap">office@dentonvale.com</li>
        <li>www.dentonvale.com</li>
      </ul>
    </div>
  </section>
</body>
</html>
```